Homebuilder & Remodeling Firm looking for archectrual looking website

We are a Custom home building & remodeling company since 1986 and would like to launch a website.Tom Halvery the principle of the firm is a graduate of Marlow Univesity school of architecture and draws his own designs and working drawings. and has done many residential, single and multi family projects in the Dallas Ft Worth Metroplex. We want our website to be architectural in design and visually appealing. We will eventually have photos to provide for you. The message we want to communicate is we have current update knowledge with trends, and longevity in experience. Our message is that we are a firm that designs and remodels fully through and we provide a well executed custom home that is unique to each client. The Homes that we build are unique ,authentic and sustainable architectural styles such as mid century modern, contemporary, transitional and they are sophisticated homes to compliment individual lifestyles of our clients. We have a passion for construction and an attention to detail that makes your dreams come to life. We listen to each clients every need in functionality and form and take them from pre-construction to post-construction follow -up.
We help you invest in your home. Thoughts Create Reality

EXAMPLES OF WEBSITES THAT WE LIKE. PLEASE DO
MORE CONTEMPORARY, SLEEK, ARCHITECTURAL

* Please make the LOGO a bigger part of design

http://penwickgroup.build/
https://www.quillorn.co/
http://vantrelmodernhomes.com/
http://www.neilcorradesign.com/
http://www.fennickolde.com/
http://ravodesignstudios.com/about
http://mendaleigc.com/

thank you,

Reason: We have many clients asking to see our website and re ready to launch something for them to look at

Target Market(s)

Home owners, home buyers, interior designers, All ages

Industry/Entity Type

Builders

Coding

Coded - Design and coding required

Number of Pages Required

5+ page

Font styles to use
Sans Serif

Requirements
Must have
• HTML5 OR PHP
• graphic artist must speak English:
• *Visually appealing, user friendly,
• * the website should reflect the stability and integrity of the company since it has been in business for over 30 years
• * a sophistication and refinement is our mandate.
Should not have
• Too busy, too much going on, we want more minimal in design and artsitic

```html
<!DOCTYPE html>
<html lang="en">
<head>
<meta charset="utf-8">
<title>Halvery Development — Custom Homes &amp; Remodeling</title>
<link rel="stylesheet" href="https://fonts.googleapis.com/css2?family=Lato:wght@400;700&family=Questrial&display=swap">
<style>
  :root {
    --white: #ffffff;
    --navy: #1f2f55;
    --grey-text: #5d5d5d;
    --muted: #a7a7a7;
    --divider: #e6e6e6;
    --foliage: #6f8a6c;
    --stone: #6e6259;
    --glass-dark: #3a4048;
    --frame: #2c3036;
    --wall: #a8b3c1;
    --wall-light: #b8c2cf;
    --door: #3b3f46;
    --ceiling: #7d8896;
  }
  * { box-sizing: border-box; margin: 0; padding: 0; }
  html, body { width: 1200px; height: 577px; overflow: hidden; }
  body { position: relative; font-family: "Lato", sans-serif; background: var(--white); }

  .hero {
    position: absolute; inset: 0;
    background:
      linear-gradient(180deg, rgba(60,66,76,0.45) 0%, rgba(60,66,76,0) 28%, rgba(0,0,0,0) 80%, rgba(40,44,50,0.25) 100%),
      linear-gradient(90deg,
        var(--foliage) 0%,
        #7f8f86 9%,
        var(--stone) 15%,
        #5f5650 22%,
        var(--glass-dark) 27%,
        #4d5560 38%,
        var(--frame) 47%,
        #6c7684 54%,
        var(--wall) 62%,
        var(--wall-light) 78%,
        #a3afbd 86%,
        var(--door) 96%,
        #2e3238 100%);
  }

  .site-header {
    position: absolute; left: 0; top: 0; width: 840px; height: 79px;
    background: var(--white);
    box-shadow: 0 1px 3px rgba(0,0,0,0.18);
  }
  .brand { position: absolute; left: 34px; top: 18px; display: flex; align-items: center; gap: 10px; }
  .brand-square { width: 30px; height: 42px; background: var(--navy); }
  .brand-text { display: flex; flex-direction: column; padding-top: 6px; }
  .brand-name {
    font-family: "Questrial", sans-serif; font-variant: small-caps;
    font-size: 18px; line-height: 18px; color: var(--navy); letter-spacing: 0.1px;
    white-space: nowrap;
  }
  .brand-tagline {
    font-size: 6.5px; letter-spacing: 2.5px; color: var(--muted); margin-top: 2px; white-space: nowrap;
  }

  .main-nav {
    position: absolute; left: 321px; top: 36px; width: 430px;
    display: flex; justify-content: space-between;
  }
  .main-nav a {
    font-size: 11px; letter-spacing: 1.9px; color: var(--grey-text);
    text-decoration: none; text-transform: uppercase; white-space: nowrap;
  }
  .nav-divider { position: absolute; left: 769px; top: 17px; width: 5px; height: 45px; background: var(--divider); }
  .share { position: absolute; left: 789px; top: 34px; font-size: 10px; font-weight: 700; color: #111; }

  .hero-mark { position: absolute; left: 398px; top: 214px; width: 46px; height: 46px; background: var(--white); }
  .hero-title {
    position: absolute; left: 140px; top: 302px;
    font-family: "Questrial", sans-serif; font-variant: small-caps; font-weight: 400;
    font-size: 53px; line-height: 56px; color: var(--white); letter-spacing: 0.3px;
    white-space: nowrap; text-shadow: 0 1px 6px rgba(0,0,0,0.2);
  }

  .slide-dots { position: absolute; left: 17px; top: 288px; display: flex; flex-direction: column; gap: 6px; }
  .slide-dots span { width: 9px; height: 9px; border-radius: 50%; background: var(--white); }
  .slide-dots span.is-active { background: transparent; border: 1.5px solid var(--white); }

  .slide-arrows { position: absolute; left: 1083px; top: 536px; display: flex; gap: 20px; }
</style>
</head>
<body>
  <div class="hero" role="img" aria-label="Photograph of a modern home balcony with stone cladding, dark window frames, a glass railing and a bright white interior room"></div>

  <header class="site-header">
    <div class="brand">
      <span class="brand-square"></span>
      <div class="brand-text">
        <span class="brand-name">Halvery Development</span>
        <span class="brand-tagline">CUSTOM HOMES • REMODELING</span>
      </div>
    </div>
    <nav class="main-nav">
      <a href="#">Home</a>
      <a href="#">Available Now</a>
      <a href="#">About Us</a>
      <a href="#">Affiliate</a>
      <a href="#">Contact</a>
    </nav>
    <span class="nav-divider"></span>
    <span class="share">Share</span>
  </header>

  <span class="hero-mark"></span>
  <h1 class="hero-title">Halvery Development</h1>

  <div class="slide-dots">
    <span class="is-active"></span><span></span><span></span><span></span>
  </div>

  <div class="slide-arrows">
    <svg width="18" height="12" viewBox="0 0 18 12" aria-label="Previous slide"><path d="M17 6H2M6 1.5L1.5 6 6 10.5" stroke="#fff" stroke-width="2" fill="none"/></svg>
    <svg width="18" height="12" viewBox="0 0 18 12" aria-label="Next slide"><path d="M1 6h15M12 1.5L16.5 6 12 10.5" stroke="#fff" stroke-width="2" fill="none"/></svg>
  </div>
</body>
</html>
```